Lucky Orbit Fun Casino Entertainment

Looking to update my business card and make it look more modern, stand out and eye catching.
We are are fun casino business in Australia (primarily Sydney). Blackjack and Roulette are our most popular games although we have pretty much every game available for hire that you would find in a real casino. The final design would need to be sleek and appeal to the more upmarket corporate sector.
We mainly cater for Corporate Events, Private Parties, Fundraising Events, Team Building, Poker Tournaments
I think I'd prefer the colour Black.

Target Market(s)

High-end Corporate

Industry/Entity Type

Events

Contact Information for Business Card

Dale Hutchins
Director
1300 482 617
0431 758 209
info@luckyorbit.com.au
www.luckyorbit.com.au
Facebook & Instagram @luckyorbitshows (proper social icons preferred)

Colors
000000
0255a3

Requirements
Must have
• Front side:
• Logo
• Contact details
• 'Australia's #1 Fun Casino Specialists'
• Back:
• Logo
Nice to have
• Back:
• Corporate Events
• Private Parties
• Poker Tournaments
• Fundraising
• Props & Theming
• Photo Booth
• Horse Racing Events
• The Vegas Sign attached, maybe on the back of the card in the background...?

```html
<!DOCTYPE html>
<html lang="en">
<head>
<meta charset="utf-8">
<title>Lucky Orbit – Business Card</title>
<link href="https://fonts.googleapis.com/css2?family=Roboto:wght@400;500;700&display=swap" rel="stylesheet">
<style>
  :root {
    --stage: #2a2a2a;
    --black: #000000;
    --blue: #0255a3;
    --charcoal: #1c1c1c;
    --ink: #1a1a1a;
    --paper: #ffffff;
    --rule: #bdbdbd;
  }
  * { box-sizing: border-box; margin: 0; padding: 0; }
  html, body {
    width: 1200px; height: 1108px; overflow: hidden;
    background: var(--stage);
    font-family: "Roboto", Arial, sans-serif;
  }
  .canvas { position: relative; width: 1200px; height: 1108px; }

  .card {
    position: absolute; left: 220px; width: 760px; height: 434px;
    box-shadow: 0 14px 30px rgba(0,0,0,.45);
    overflow: hidden;
  }

  /* Back side */
  .card--back { top: 90px; background: var(--black); }
  .card--back .brand {
    position: absolute; left: 0; right: 0; top: 100px;
    display: flex; align-items: center; justify-content: center; gap: 18px;
  }
  .brand__dot {
    width: 74px; height: 74px; border-radius: 50%; background: var(--blue); flex: none;
  }
  .brand__name {
    font-weight: 700; font-size: 50px; letter-spacing: 1px; text-transform: uppercase;
    white-space: nowrap;
  }
  .card--back .brand__name { color: var(--paper); }
  .services {
    position: absolute; left: 0; right: 0; top: 258px; height: 104px;
    background: var(--blue); color: var(--paper);
    display: flex; flex-direction: column; justify-content: center; align-items: center;
    gap: 8px; font-size: 21px;
  }
  .services__line span + span::before {
    content: "\2022"; color: var(--paper); margin: 0 10px;
  }

  /* Front side */
  .card--front { top: 614px; background: var(--paper); }
  .card--front .brand {
    position: absolute; left: 40px; top: 120px;
    display: flex; align-items: center; gap: 14px;
  }
  .card--front .brand__dot { width: 60px; height: 60px; }
  .card--front .brand__name { color: var(--black); font-size: 40px; }
  .tagline {
    position: absolute; left: 40px; top: 236px;
    font-size: 19px; color: var(--ink); white-space: nowrap;
  }
  .divider {
    position: absolute; left: 410px; top: 90px; width: 2px; height: 250px;
    background: linear-gradient(to bottom, transparent, var(--rule) 30%, var(--rule) 70%, transparent);
    transform: rotate(15deg);
  }
  .contact { position: absolute; left: 470px; top: 96px; color: var(--ink); }
  .contact__name {
    color: var(--blue); font-weight: 700; font-size: 34px; text-transform: uppercase;
    white-space: nowrap;
  }
  .contact__role { font-weight: 500; font-size: 20px; letter-spacing: .5px; margin-bottom: 16px; color: var(--black); }
  .contact__list { list-style: none; }
  .contact__item {
    display: flex; align-items: center; gap: 12px; font-size: 21px; line-height: 32px;
    white-space: nowrap;
  }
  .contact__icon { width: 20px; height: 20px; fill: var(--blue); flex: none; }
</style>
</head>
<body>
<main class="canvas">

  <section class="card card--back" aria-label="Business card back">
    <div class="brand">
      <span class="brand__dot"></span>
      <span class="brand__name">Lucky Orbit</span>
    </div>
    <div class="services">
      <p class="services__line"><span>Corporate Events</span><span>Private Parties</span><span>Poker Tournaments</span></p>
      <p class="services__line"><span>Fundraising</span><span>Props &amp; Theming</span><span>Photo Booth</span><span>Horse Racing Events</span></p>
    </div>
  </section>

  <section class="card card--front" aria-label="Business card front">
    <div class="brand">
      <span class="brand__dot"></span>
      <span class="brand__name">Lucky Orbit</span>
    </div>
    <p class="tagline">Australia's #1 Fun Casino Specialists</p>
    <span class="divider"></span>

    <div class="contact">
      <h1 class="contact__name">Dale Hutchins</h1>
      <p class="contact__role">DIRECTOR</p>
      <ul class="contact__list">
        <li class="contact__item">
          <svg class="contact__icon" viewBox="0 0 24 24"><path d="M6.6 10.8a15 15 0 0 0 6.6 6.6l2.2-2.2c.3-.3.7-.4 1-.2 1.1.4 2.3.6 3.6.6.6 0 1 .4 1 1V20c0 .6-.4 1-1 1A17 17 0 0 1 3 4c0-.6.4-1 1-1h3.5c.6 0 1 .4 1 1 0 1.3.2 2.5.6 3.6.1.3 0 .7-.2 1z"/></svg>
          1300 482 617
        </li>
        <li class="contact__item">
          <svg class="contact__icon" viewBox="0 0 24 24"><path d="M7 1h10a2 2 0 0 1 2 2v18a2 2 0 0 1-2 2H7a2 2 0 0 1-2-2V3a2 2 0 0 1 2-2zm0 3v14h10V4zm5 15.2a1.2 1.2 0 1 0 0 2.4 1.2 1.2 0 0 0 0-2.4z"/></svg>
          0431 758 209
        </li>
        <li class="contact__item">
          <svg class="contact__icon" viewBox="0 0 24 24"><path d="M2 5h20v14H2zm2 2v.5l8 5 8-5V7zm0 2.8V17h16V9.8l-8 5z"/></svg>
          info@luckyorbit.com.au
        </li>
        <li class="contact__item">
          <svg class="contact__icon" viewBox="0 0 24 24"><path d="M12 2a10 10 0 1 0 0 20 10 10 0 0 0 0-20zm6.9 6h-3a15 15 0 0 0-1.3-3.9A8 8 0 0 1 18.9 8zM12 4c.8 1.2 1.5 2.5 1.9 4h-3.8c.4-1.5 1.1-2.8 1.9-4zM4.3 14a8 8 0 0 1 0-4h3.4a16 16 0 0 0 0 4zm.8 2h3a15 15 0 0 0 1.3 3.9A8 8 0 0 1 5.1 16zm3-8h-3a8 8 0 0 1 4.3-3.9C8.8 5.3 8.4 6.6 8.1 8zM12 20c-.8-1.2-1.5-2.5-1.9-4h3.8c-.4 1.5-1.1 2.8-1.9 4zm2.3-6H9.7a14 14 0 0 1 0-4h4.6a14 14 0 0 1 0 4zm.3 5.9c.6-1.2 1-2.5 1.3-3.9h3a8 8 0 0 1-4.3 3.9zm1.7-5.9a16 16 0 0 0 0-4h3.4a8 8 0 0 1 0 4z"/></svg>
          www.luckyorbit.com.au
        </li>
      </ul>
    </div>
  </section>

</main>
</body>
</html>
```